Brise haute coffee - Label design

Watchout: Keep in mind while you submit it needs to be a LABEL (that will be sticked on brown kraft 250 g side gusset coffee pouches). No custom pack for time being (need more scale to custom print pack).

Looking for a label design for my new Doux Vent collection of freshly roasted, single origin specialty coffee. Brand name is Brise Haute (it means red earth and alludes to the soil coffee grows on at high altitude in Africa. It also alludes to the red color of the coffee fruit). Brand selling line is "Pure Origin Coffee". Label to go as stickers on 250 g side gusset coffee pouches in Kraft brown paper (will print labels and stick on packs, packs are 80 mm wide and 260 mm long). This is a relatively complex project comprising the "brise haute" brand logo (funded separately, winner will have the job), the "Doux Vent" collection visual identity, iconic assets for brand and collection recognition across lineup, educational visual icons, text placeholders. It needs to combine hard point visual elements and soft points (text placeholder) which I can easily edit on need basis (text needs to be "outlines" for easy editing after submission). Winner of label submission gets to design brand logo. I will ultimately need 3 different labels for our Doux Vent collection, one for each continent our coffee comes from (Africa, Asia, Latin America). This pitch should focus on the Africa one only. Winner will then have opportunity to design the other ones in consistent way.

BRIEF:
We roast single origin, high quality specialty coffee from high altitude estates in Africa (volcanic slopes in Congo and Burundi, Highlands in Ethiopia and Kenya) Design need to induce the premiumness of the proposition (this is a collection called "Doux Vent"), as well the the unique geographical origins of our coffee (without being too specific as we want to use same label for all our African origins) -oversized shape of continent in background + some visuals conveying the African roots could work well. It needs to create a mental Journey "back to the origins" - of mankind, of unique terroirs creating the best coffee, of our unspoilt roots. So the Journey themes is critical (to be expressed by the telegram type of font, by the way Africa is brought to life,etc.). At the same time keep in mind label space is limited (label stickers go on 250 g coffee pouches made in kraft brown paper) and we want to have a pure design, which leaves room to the text placeholder (see below) and is easily recognizable and reapplicable across the SKUs (we will add Asia and Latin America packs once we lock Africa). As such we need to strike right balance between visual differentiation by origin (Africa, Asia, Latin America) and common iconic assets for brand recognition and lineup harmonization (same font, same way the continent is brought to life, same structure of the label, differentiation by color background,etc.).

We need placeholder for text that will specify exact name of estate, county of origin, coffee type, roasting level and tasting notes. Here I will allow myself some creative direction: it should be in the format of a vintage luggage tag (see attached examples) where we can edit content in Telegram font (our coffee sourcing changes often). We will need to assess if the tag remains standard across collection, or whether we are able to give it a visual twist for each origin (Africa, Asia, Latin America). That would be nicer (see Morvelin "Stamps" example), but priority of the text placeholder is clarity of information above anything else.

Last nice to have (if it time allows) we need educational visual icons (ideally as separate small round labels we can stick on the pack above the main label) for recommended brewing method (filter, espresso, italian moka, french press).

Reason: Still looking for the design in line with brief. Will send feedback to the top 3 routes today.

Target Market(s)

Switzerland

Industry/Entity Type

Coffee Shop

Logo Text

Brise haute -Pure Origin Coffee

Font styles to use
Other font styles liked:
• TELEGRAM type of font to induce geographical journey, single origin,.. For the "luggage tag" placeholder

Requirements
Must have
• - Brand name: Brise Haute. Brand selling line: Pure Origin Coffee. Brand Logo: winner of label submission gets to design brand logo
• - Collection name: DOUX VENT (written, I can see well as a vertical block). name of SKU: AFRICA (visualized a must, written tbc).
• - Text place holder (vintage luggage tag in telegram font) : we will show there name of estate, country of origin, tasting notes. I could see nicely a baggage tag format, where we fill in the details in telegram type of font.
• - 100% single origin Arabica (at the bottom)
• - 250 g (at the bottom)
• Technical Specs:
• A. Artwork must be supplied in either Adobe illustrator or Adobe Photoshop files or Coral Draw files
• B. Create all text in artwork in ‘ outlines ’
• C. The resolution of photographic image files must be no less than 350 dpi
• D. Never flatten the file as we require all layers
• E. All Photoshop image files should be linked and attached. Never flatten the layers and do not change the directory
• F. Create the images with CMYK colour mode ( RGB colour mode is not for printing)
• G. If you are going to use a spot colour please reference the Pantone ( PMS #)
• H. Designate all ‘Transparent’ areas in the artwork with a custom Pantone colour as well as designating the layer’s name as ‘ Transparent’. Please indicate specifically which pantone colour is designated for the ‘transparent’ area.
• I. Reduce any barcodes to 85% as a minimum scale
Nice to have
• - educational simple visual icons on recommended brewing method (filer, italian moka, french press or espresso) as additional small stickers to stick above main label

```html
<!DOCTYPE html>
<html lang="en">
<head>
<meta charset="utf-8">
<title>Brise Haute – Doux Vent Collection Label</title>
<link rel="stylesheet" href="https://fonts.googleapis.com/css2?family=Oswald:wght@300;400&family=Oranienbaum&family=Courier+Prime&display=swap">
<style>
  :root {
    --backdrop: #e8e6e3;
    --kraft: #c9a892;
    --paper: #ffffff;
    --espresso: #3a2e26;
    --rust: #8e3a1f;
    --rust-band: #93391e;
    --map-sand: #fbe8d0;
    --pattern-ochre: #f2b548;
    --ink-dark: #2a2a2a;
  }
  * { box-sizing: border-box; margin: 0; padding: 0; }
  html, body { width: 1012px; height: 1200px; overflow: hidden; }
  body { background: var(--backdrop); position: relative; font-family: "Oswald", sans-serif; }

  .main-label {
    position: absolute; left: 274px; top: 78px; width: 354px; height: 1040px;
    background: var(--kraft);
  }
  .main-label__panel {
    position: absolute; left: 24px; top: 0; width: 306px; height: 1016px;
    background: var(--paper); overflow: hidden;
  }
  .continent-map {
    position: absolute; left: 2px; top: 137px; width: 304px; height: 330px;
    background: radial-gradient(ellipse at 45% 45%, var(--map-sand) 55%, rgba(251,232,208,0) 72%);
  }
  .collection-band {
    position: absolute; left: 88px; top: 22px; width: 132px; height: 357px;
    background: var(--espresso); border: 2px solid var(--rust);
    border-top: none; border-radius: 0 0 10px 10px;
  }
  .brand-seal {
    position: absolute; left: 79px; top: 207px; width: 150px; height: 150px;
    border-radius: 50%; background: var(--paper); border: 2px solid var(--rust);
    display: flex; align-items: center; justify-content: center;
  }
  .brand-name {
    font-family: "Oranienbaum", serif; color: var(--rust);
    font-size: 24px; letter-spacing: 1px;
  }
  .collection-title {
    position: absolute; left: 0; right: 0; top: 480px; text-align: center;
    color: var(--rust); font-weight: 400; font-size: 46px; letter-spacing: 3px; line-height: 1;
  }
  .collection-subtitle {
    position: absolute; left: 0; right: 0; top: 536px; text-align: center;
    color: var(--rust); font-weight: 300; font-size: 16px; letter-spacing: 7px; padding-left: 7px;
  }
  .origin-claim {
    position: absolute; left: 34px; width: 236px; top: 688px; text-align: center;
    color: var(--ink-dark); font-weight: 300; font-size: 17px; line-height: 1.2;
  }
  .origin-claim__rule {
    position: absolute; left: 34px; width: 236px; top: 720px; height: 3px; background: var(--rust);
  }
  .tagline {
    position: absolute; left: 34px; width: 236px; top: 730px; text-align: center;
    font-family: "Oranienbaum", serif; color: var(--rust); font-size: 25px;
  }
  .tagline__rules {
    position: absolute; left: 34px; width: 236px; top: 763px; height: 1px;
    display: flex; justify-content: space-between;
  }
  .tagline__rules span { display: block; width: 104px; height: 1px; background: var(--rust); }
  .tagline__rules span:last-child { width: 106px; }
  .heritage-pattern {
    position: absolute; left: 0; top: 818px; width: 306px; height: 160px;
    background: linear-gradient(180deg, #f6cf86 0%, var(--pattern-ochre) 50%, #f6cf86 100%);
    opacity: 0.85;
  }
  .weight-bar {
    position: absolute; left: 0; top: 979px; width: 306px; height: 37px;
    background: var(--rust-band); color: var(--paper);
    font-family: "Courier Prime", monospace; font-size: 20px;
    display: flex; align-items: center; justify-content: flex-end; padding-right: 14px;
  }

  .seal-sticker {
    position: absolute; left: 685px; top: 118px; width: 191px; height: 236px;
    background: var(--kraft);
  }
  .seal-sticker__disc {
    position: absolute; left: 9px; top: 10px; width: 174px; height: 174px;
    border-radius: 50%; background: var(--paper); border: 2px solid var(--rust);
    display: flex; align-items: center; justify-content: center;
  }
  .seal-sticker__disc .brand-name { font-size: 27px; }
  .seal-sticker__tagline {
    position: absolute; left: 0; right: 0; top: 200px; text-align: center;
    font-family: "Courier Prime", monospace; font-size: 13px; color: var(--ink-dark);
  }
</style>
</head>
<body>
  <section class="main-label">
    <div class="main-label__panel">
      <div class="continent-map" role="img" aria-label="Oversized outline of the African continent in pale sand"></div>
      <div class="collection-band"></div>
      <div class="brand-seal"><span class="brand-name">Brise Haute</span></div>
      <h1 class="collection-title">DOUX VENT</h1>
      <p class="collection-subtitle">COLLECTION</p>
      <p class="origin-claim">100% SINGLE ORIGIN ARABICA</p>
      <div class="origin-claim__rule"></div>
      <p class="tagline">Pure Origin Coffee</p>
      <div class="tagline__rules"><span></span><span></span></div>
      <div class="heritage-pattern" role="img" aria-label="Ochre African tribal border pattern"></div>
      <div class="weight-bar">250 g</div>
    </div>
  </section>

  <aside class="seal-sticker">
    <div class="seal-sticker__disc"><span class="brand-name">Brise Haute</span></div>
    <p class="seal-sticker__tagline">Pure Origin Coffee</p>
  </aside>
</body>
</html>
```